Black Granite Web Design Project

We are looking for a design for a new company that will be selling Black Granite slabs and tiles. We will be selling to both end-consumers and granite installers. We have already settled on a logo and hopefully this will give an idea of what we like in our designs. We are not going to be selling online but want people to call us so the site is basically an enhanced business card. We will be focusing a lot on SEO so the design will have to keep that in mind.

We would like to keep the design in 1024x768 to make it easily view-able on all devices.

Regarding navigation there should only be a few sub-pages, like "Granite Slabs", "Granite Tiles", "Delivery", "Contact"

Aside from that we are open to designs. One idea we did have was to personalize the site and have a person there somehow to represent the company, making the user feel there are real people behind this site. This is just an idea and not a must.

The name of the company and site is "Copper Ridge Pietra"

Thanks
Updates

Hello All,

Thanks for the great designs. There are some good looking designs that show beautiful kitchens but this site is made for the granite installers and not the retail consumers. So in order not to to confuse the buyers I would like to keep this as much about the raw products as possible. The raw products being the granite slabs, thereby making it obvious we don't sell granite counter tops. 

This design will really be the identity of this company so it is important we get the right message across on this index page and that this page is as complete as possible.

Again, thanks for all the work being put into this.

Target Market(s)

The target audience is granite installers or companies that would with granite slabs.

Industry/Entity Type

Business

```html
<!DOCTYPE html>
<html lang="en">
<head>
<meta charset="utf-8">
<title>Copper Ridge Pietra – Black Granite Slabs and Tiles</title>
<link href="https://fonts.googleapis.com/css2?family=Play:wght@400;700&family=Arimo:wght@400;700&display=swap" rel="stylesheet">
<style>
:root{
  --stone-dark:#0d0d0d;
  --stone-mid:#1c1c1c;
  --paper:#ffffff;
  --hero-bg:#eeeeee;
  --card-bg:#f2f2f2;
  --panel-grey:#ececec;
  --text-dark:#222222;
  --text-body:#3a3a3a;
  --accent-green:#3d5e25;
  --accent-green-dark:#2b4419;
  --nav-top:#3a3a3a;
  --nav-bottom:#050505;
  --field-border:#cfcfcf;
  --placeholder:#a8a8a8;
  --footer-top:#4a4a4a;
  --footer-bottom:#0a0a0a;
}
*{margin:0;padding:0;box-sizing:border-box}
html,body{width:1200px;height:1124px;overflow:hidden;background:var(--paper)}
body{position:relative;font-family:"Arimo",Arial,sans-serif;color:var(--text-dark)}
.page-backdrop{position:absolute;left:0;top:0;width:1200px;height:515px;background:radial-gradient(circle at 30% 40%,var(--stone-mid),var(--stone-dark) 70%)}
.site-header{position:absolute;left:76px;top:0;width:1048px;height:142px;background:var(--paper)}
.brand{position:absolute;left:33px;top:50px;display:flex;align-items:center;gap:10px;font-family:"Play",sans-serif;font-weight:700;font-size:22px;color:var(--text-dark)}
.brand-square{width:26px;height:26px;background:var(--text-dark)}
.phone-box{position:absolute;left:810px;top:53px;width:225px;height:50px;background:var(--panel-grey);display:flex;align-items:center;gap:14px;padding-left:14px;font-family:"Arimo",sans-serif;font-size:24px;color:var(--text-dark)}
.main-nav{position:absolute;left:76px;top:142px;width:1048px;height:48px;background:linear-gradient(var(--nav-top),var(--nav-bottom));display:flex}
.main-nav a{display:flex;align-items:center;justify-content:center;height:48px;color:#fff;text-decoration:none;font-family:"Play",sans-serif;font-weight:700;font-size:17px;letter-spacing:.5px;border-right:2px solid #fff}
.main-nav a:last-child{border-right:none;justify-content:flex-start;padding-left:28px}
.hero{position:absolute;left:76px;top:190px;width:1048px;height:325px;background:var(--hero-bg);overflow:hidden}
.hero-kicker{position:absolute;left:46px;top:42px;font-family:"Play",sans-serif;font-size:27px;color:var(--text-dark)}
.hero-title{position:absolute;left:46px;top:78px;font-family:"Play",sans-serif;font-weight:400;font-size:33px;line-height:39px;color:var(--text-dark)}
.hero-text{position:absolute;left:46px;top:160px;width:378px;font-size:14px;line-height:16px;text-align:justify;color:var(--text-body)}
.btn-learn{position:absolute;left:47px;top:239px;width:232px;height:41px;background:linear-gradient(var(--accent-green),var(--accent-green-dark));color:#fff;display:flex;align-items:center;justify-content:center;gap:14px;font-family:"Play",sans-serif;font-weight:700;font-size:17px;letter-spacing:.5px}
.hero-photo{position:absolute;left:0;top:0}
.slider-control{position:absolute;left:489px;top:290px;width:56px;height:56px;border-radius:50%;background:#5a5a5a}
.product-card{position:absolute;width:327px;height:328px;background:var(--card-bg)}
.card-slab{left:94px;top:545px}
.card-tile{left:447px;top:548px}
.card-head{height:58px;background:linear-gradient(#353535,#6a6a6a);color:#fff;font-family:"Play",sans-serif;font-weight:700;font-size:24px;display:flex;align-items:center;justify-content:center}
.card-photo{height:131px}
.slab-photo{background:linear-gradient(160deg,#4a4d4a,#1f211f 60%,#5a5c5a)}
.tile-photo{background:linear-gradient(#6b6b6b,#0b0b0b 20%,#0b0b0b 80%,#6b6b6b)}
.card-text{padding:18px 20px 0 20px;font-size:14px;line-height:16px;text-align:justify;color:var(--text-body)}
.card-more{position:absolute;right:26px;bottom:28px;display:flex;align-items:center;gap:8px;font-family:"Play",sans-serif;font-weight:700;font-size:17px;color:var(--accent-green-dark)}
.quote-form{position:absolute;left:814px;top:560px;width:284px}
.quote-title{font-family:"Play",sans-serif;font-size:28px;font-weight:400;margin-left:5px;margin-bottom:16px;color:var(--text-dark)}
.field{display:block;width:284px;height:29px;border:1px solid var(--field-border);padding:6px 10px;font-size:13px;color:var(--placeholder);margin-bottom:16px;background:#fff}
.field-message{height:70px;margin-bottom:18px}
.btn-send{display:block;margin-left:85px;width:150px;height:33px;background:#4a4a4a;color:#fff;font-size:17px;font-weight:700;border:none;box-shadow:2px 2px 3px rgba(0,0,0,.35);text-align:center;line-height:33px}
.site-footer{position:absolute;left:0;top:933px;width:1169px;height:191px;background:linear-gradient(var(--footer-top),var(--footer-bottom) 55%);color:#fff}
.footer-name{position:absolute;left:115px;top:24px;font-family:"Play",sans-serif;font-weight:700;font-size:20px}
.footer-address{position:absolute;left:115px;top:62px;width:246px;font-size:14px;line-height:17px;text-align:justify}
.footer-contact{position:absolute;left:117px;top:121px;font-size:14px;line-height:18px}
.footer-divider{position:absolute;left:401px;top:27px;width:1px;height:149px;background:#6a6a6a}
.social{position:absolute;top:56px;width:33px;height:33px;background:#d8d8d8;border:2px solid #8a8a8a}
.social-one{left:454px}
.social-two{left:498px}
.footer-brand{position:absolute;left:945px;top:19px;width:168px;height:90px;border:1px solid #333;display:flex;align-items:center;justify-content:center;font-family:"Play",sans-serif;font-weight:700;font-size:15px}
.copyright{position:absolute;right:56px;top:155px;font-size:11px}
</style>
</head>
<body>
<div class="page-backdrop"></div>

<header class="site-header">
  <div class="brand"><span class="brand-square"></span>Copper Ridge Pietra</div>
  <div class="phone-box">
    <svg width="26" height="24" viewBox="0 0 26 24" aria-hidden="true">
      <path d="M2 9c0-5 22-5 22 0l-5 1-1-3H8L7 10z" fill="#222"/>
      <path d="M6 12h14l3 9H3z" fill="#222"/>
      <circle cx="13" cy="16" r="3" fill="#ececec"/>
    </svg>
    <span>555 014 2287</span>
  </div>
</header>

<nav class="main-nav">
  <a href="#" style="width:106px">—HOME—</a>
  <a href="#" style="width:188px">GRANITE SLABS</a>
  <a href="#" style="width:170px">GRANITE TILES</a>
  <a href="#" style="width:150px">DELIVERY</a>
  <a href="#" style="flex:1">CONTACT</a>
</nav>

<section class="hero">
  <svg class="hero-photo" width="1048" height="325" viewBox="0 0 1048 325" role="img" aria-label="Polished black granite slab with white and grey veining">
    <defs>
      <linearGradient id="slabGlow" x1="0" y1="0" x2="1" y2="1">
        <stop offset="0" stop-color="#2a2e2e"/>
        <stop offset=".5" stop-color="#0e1111"/>
        <stop offset="1" stop-color="#3a3d3d"/>
      </linearGradient>
    </defs>
    <polygon points="631,55 1048,1 1048,325 609,325" fill="url(#slabGlow)"/>
  </svg>
  <p class="hero-kicker">We are suppliers of</p>
  <h1 class="hero-title">BLACK GRANITE SLAB<br>AND BLACK GRANITE TILES</h1>
  <p class="hero-text">Lorem ipsum dolor sit amet cons ectetuer adipiscing elit praesent vestibulu moles lacus aenean nonummy.Lorem ipsum dolor sit amet cons ectetuer adipiscing elit praesent vestibulu moles lacus aenean nonummy.</p>
  <a class="btn-learn">LEARN MORE
    <svg width="20" height="16" viewBox="0 0 20 16" aria-hidden="true"><path d="M1 8h16M11 2l6 6-6 6" stroke="#fff" stroke-width="3" fill="none"/></svg>
  </a>
  <div class="slider-control">
    <svg width="56" height="36" viewBox="0 0 56 36" aria-hidden="true"><path d="M24 14l-6 6 6 6M32 14l6 6-6 6" stroke="#fff" stroke-width="3" fill="none"/><path d="M28 12v18" stroke="#888" stroke-width="1"/></svg>
  </div>
</section>

<article class="product-card card-slab">
  <h2 class="card-head">GRANITE SLAB</h2>
  <div class="card-photo slab-photo" role="img" aria-label="Black granite slab resting in a warehouse"></div>
  <p class="card-text">Lorem ipsum dolor sit amet cons ectetuer adipiscing elit praesent vestibulu moles lacus aenean nonummy.</p>
  <span class="card-more">MORE <svg width="16" height="12" viewBox="0 0 16 12" aria-hidden="true"><path d="M0 6h13M9 1l5 5-5 5" stroke="#2b4419" stroke-width="2" fill="none"/></svg></span>
</article>

<article class="product-card card-tile">
  <h2 class="card-head">GRANITE TILE</h2>
  <div class="card-photo tile-photo" role="img" aria-label="Six polished black granite tiles laid in a grid"></div>
  <p class="card-text">Lorem ipsum dolor sit amet cons ectetuer adipiscing elit praesent vestibulu moles lacus aenean nonummy.</p>
  <span class="card-more">MORE <svg width="16" height="12" viewBox="0 0 16 12" aria-hidden="true"><path d="M0 6h13M9 1l5 5-5 5" stroke="#2b4419" stroke-width="2" fill="none"/></svg></span>
</article>

<form class="quote-form">
  <h2 class="quote-title">Get a free quote</h2>
  <span class="field">Name</span>
  <span class="field">Email</span>
  <span class="field field-message">Message</span>
  <span class="btn-send">Send</span>
</form>

<footer class="site-footer">
  <h3 class="footer-name">Copper Ridge Pietra</h3>
  <p class="footer-address">Ed. Pedra Alta, Sala 42, Rua das Pedras 19, Centro, Vila Serena, VS, CEP-98765-432</p>
  <p class="footer-contact">Phone: 555 014 2287<br>Email: hello@copperridgepietra.com</p>
  <div class="footer-divider"></div>
  <span class="social social-one"></span>
  <span class="social social-two"></span>
  <div class="footer-brand">Copper Ridge Pietra</div>
  <p class="copyright">Copyright 2013 Copper Ridge Pietra. All right reserved.</p>
</footer>
</body>
</html>
```